Business Card / Appointment Card for Physician

On one side it should give the logo, address, and contact information, and on the other side it should br an Appointment card.

One Side:
Logo (see attached files)
Board Certified American Orthopedic Surgery

1487 Harrowgate Ave.
Suite KM7
Bronx, NY 10527
Tel: (718) 552 - 1948
Fax: (718) 552 - 7210

628 Fourth Ave.
Suite 42
New York, NY 10087
Tel: (212) 734 - 2815

Second Side:
Appointment
give them a choice of Bronx or Mahattan office
For:
Date:
Time:

If you are unable to keep your appointment, please call (718) 263-5102 24hrs in advance.

Target Market(s)

People that need orthopedic surgery

Industry/Entity Type

Business

Contact Information for Business Card

smart and attractive

Requirements
Must have
• logo
• contact information on one side, appointment information on the other

```html
<!DOCTYPE html>
<html lang="en">
<head>
<meta charset="utf-8">
<title>Hartwell Orthopaedics – Business & Appointment Card</title>
<link href="https://fonts.googleapis.com/css2?family=Work+Sans:wght@400;500&display=swap" rel="stylesheet">
<style>
  :root {
    --backdrop: #262626;
    --card: #ffffff;
    --sky: #17a3e0;
    --navy: #1d4f86;
    --leaf: #5a9e3a;
    --ocean: #1f6aa5;
    --ink: #4a4a4a;
    --photo-light: #f1f3f5;
    --photo-mid: #d9dee3;
  }
  * { margin: 0; padding: 0; box-sizing: border-box; }
  html, body {
    width: 1200px; height: 897px; overflow: hidden;
    background: var(--backdrop);
    font-family: "Work Sans", Arial, sans-serif;
  }
  .card {
    position: absolute; left: 326px; width: 543px; height: 310px;
    background: var(--card); border-radius: 18px; overflow: hidden;
  }
  .appointment-card { top: 127px; }
  .contact-card { top: 474px; }

  .appointment-title {
    position: absolute; top: 74px; left: 0; width: 100%; padding-left: 70px;
    text-align: center; color: var(--sky); font-size: 18px; font-weight: 400;
  }
  .field { position: absolute; display: flex; align-items: flex-end; color: var(--sky); font-size: 13px; }
  .field-label { margin-right: 5px; line-height: 1; }
  .field-line { border-bottom: 1px solid var(--sky); height: 1px; }
  .field-for { left: 58px; top: 115px; }
  .field-for .field-line { width: 396px; }
  .field-date { left: 57px; top: 166px; }
  .field-date .field-line { width: 389px; }
  .field-time { left: 56px; top: 216px; }
  .field-time .field-line { width: 389px; }
  .cancel-note {
    position: absolute; left: 19px; top: 281px; font-size: 12px; color: var(--ink); white-space: nowrap;
  }
  .cancel-note .highlight { color: var(--sky); }

  .brand { position: absolute; left: 24px; top: 22px; display: flex; align-items: center; gap: 8px; }
  .brand-dot { width: 16px; height: 16px; border-radius: 50%; background: var(--navy); }
  .brand-name { color: var(--navy); font-size: 18px; font-weight: 400; letter-spacing: 0.2px; }

  .doctor-name {
    position: absolute; left: 24px; top: 126px; color: var(--sky); font-size: 19px; font-weight: 500; letter-spacing: 0.5px;
  }
  .credential { position: absolute; left: 24px; top: 152px; color: var(--ink); font-size: 13.5px; }
  .office { position: absolute; left: 24px; color: var(--ink); font-size: 13.5px; line-height: 17.2px; }
  .office-bronx { top: 172px; }
  .office-manhattan { top: 245px; }
  .office .label { color: var(--sky); }

  .portrait {
    position: absolute; left: 298px; top: 12px; width: 245px; height: 290px;
    background: linear-gradient(180deg, var(--photo-light) 0%, var(--photo-mid) 100%);
  }
  .brand-bar { position: absolute; left: 0; bottom: 0; width: 100%; height: 8px; display: flex; }
  .brand-bar span { height: 100%; }
  .bar-sky { width: 179px; background: var(--sky); }
  .bar-leaf { width: 183px; background: var(--leaf); }
  .bar-ocean { flex: 1; background: var(--ocean); }
</style>
</head>
<body>
  <section class="card appointment-card">
    <h2 class="appointment-title">Appointment:</h2>
    <div class="field field-for"><span class="field-label">For:</span><span class="field-line"></span></div>
    <div class="field field-date"><span class="field-label">Date:</span><span class="field-line"></span></div>
    <div class="field field-time"><span class="field-label">Time:</span><span class="field-line"></span></div>
    <p class="cancel-note">If you are unable to keep your appointment, please <span class="highlight">call (718) 263-5102</span> 24hrs in advance.</p>
  </section>

  <section class="card contact-card">
    <div class="brand">
      <span class="brand-dot"></span>
      <span class="brand-name">HARTWELL ORTHOPAEDICS</span>
    </div>
    <h1 class="doctor-name">Dr. Daniel Hartwell</h1>
    <p class="credential">MD</p>
    <p class="office office-bronx">
      1487 Harrowgate Ave.<br>
      Suite KM7 Bronx, NY 10527<br>
      <span class="label">Tel:</span> (718) 552 - 1948<br>
      <span class="label">Fax:</span> (718) 552 - 7210
    </p>
    <p class="office office-manhattan">
      628 Fourth Ave.<br>
      Suite 42 New York, NY 10087<br>
      <span class="label">Tel:</span> (212) 734 - 2815
    </p>
    <div class="portrait" role="img" aria-label="Portrait photo of the physician in a white coat"></div>
    <div class="brand-bar"><span class="bar-sky"></span><span class="bar-leaf"></span><span class="bar-ocean"></span></div>
  </section>
</body>
</html>
```